Party flyer design

Hi ArtHive,

I need a party flyer designed incorporating my logo and the verbiage stated below for a
social get-together I'm throwing at a local martini bar and lounge in my local area.

I've attached my logo and a copy of a flyer I've seen that incorporates the look and feel I'm looking for.

Thanks

Lumora 4 presents
Velvet Hour Mixers

Join us Fridays at 11:00 PM - 2:00 AM
at At The Quill Westbrook
27315 Harlow Ridge, Suite 340
Charlotte, NC 28193

For more details email us at info@lumora4.com

```html
<!DOCTYPE html>
<html lang="en">
<head>
<meta charset="utf-8">
<title>Lumora 4 – Velvet Hour Mixers</title>
<link rel="stylesheet" href="https://fonts.googleapis.com/css2?family=Noto+Sans:wght@400;700&family=Stardos+Stencil:wght@700&family=Pinyon+Script&display=swap">
<style>
  :root {
    --red: #ee4a37;
    --orange: #f68a20;
    --deep-red: #ad2f27;
    --stamp-red: #ef5532;
    --ink: #111111;
    --stamp-ink: #3b1a0f;
    --white: #ffffff;
  }
  * { margin: 0; padding: 0; box-sizing: border-box; }
  html, body { width: 848px; height: 1200px; overflow: hidden; }
  body { font-family: "Noto Sans", Arial, sans-serif; color: var(--ink); }

  .flyer { position: relative; width: 848px; height: 1200px; background: var(--orange); overflow: hidden; }

  .band-top { position: absolute; left: 0; top: 0; width: 848px; height: 437px; background: var(--red); }
  .band-bottom { position: absolute; left: 0; top: 1020px; width: 848px; height: 180px; background: var(--red); }

  .presenter-circle {
    position: absolute; left: 72px; top: 33px; width: 376px; height: 376px;
    border-radius: 50%; background: var(--orange); border: 8px solid var(--deep-red);
    text-align: center;
  }
  .presenter-name { position: absolute; left: 0; right: 0; top: 118px; font-size: 64px; font-weight: 700; line-height: 1; }
  .presenter-name .numeral { color: var(--deep-red); }
  .presenter-verb { position: absolute; left: 0; right: 0; top: 196px; font-size: 37px; font-weight: 400; line-height: 1; }

  .brand-box {
    position: absolute; left: 476px; top: 68px; width: 300px; height: 256px;
    background: var(--white);
    display: flex; flex-direction: column; align-items: center; justify-content: center; gap: 22px;
  }
  .brand-dot { width: 116px; height: 116px; border-radius: 50%; background: var(--red); }
  .brand-name { font-size: 50px; font-weight: 700; color: var(--ink); line-height: 1; }

  .intro { position: absolute; left: 116px; top: 462px; font-size: 26px; line-height: 36px; }

  .title-stamp {
    position: absolute; left: 116px; top: 556px; width: 656px; height: 106px;
    background: var(--stamp-red); border: 8px solid var(--deep-red); border-radius: 4px;
    transform: rotate(-4deg);
    display: flex; align-items: center; justify-content: center;
  }
  .title-stamp h1 {
    font-family: "Stardos Stencil", Georgia, serif; font-weight: 700;
    font-size: 44px; letter-spacing: 2px; color: var(--stamp-ink); text-transform: uppercase;
  }

  .schedule-bar {
    position: absolute; left: 107px; top: 724px; width: 669px; height: 91px;
    background: var(--red); display: flex; align-items: center; justify-content: center;
  }
  .schedule-bar p { font-family: "Pinyon Script", cursive; font-size: 33px; color: var(--ink); }

  .venue { position: absolute; left: 171px; top: 866px; display: flex; gap: 36px; }
  .venue-pin { width: 36px; height: 54px; flex: none; }
  .venue-address { font-size: 24px; font-weight: 700; line-height: 31px; font-style: normal; }

  .contact-lead { position: absolute; left: 0; width: 848px; top: 1056px; text-align: center; font-size: 24px; font-weight: 700; padding-right: 30px; }
  .contact-mail { position: absolute; left: 241px; top: 1120px; display: flex; align-items: center; gap: 48px; }
  .mail-icon { width: 38px; height: 24px; }
  .contact-mail span { font-size: 24px; font-weight: 700; }
</style>
</head>
<body>
<main class="flyer">
  <div class="band-top"></div>
  <div class="band-bottom"></div>

  <div class="presenter-circle">
    <div class="presenter-name">Lumora <span class="numeral">4</span></div>
    <div class="presenter-verb">presents</div>
  </div>

  <div class="brand-box">
    <div class="brand-dot"></div>
    <div class="brand-name">Lumora 4</div>
  </div>

  <p class="intro">social get-together<br>at a local martini bar and lounge</p>

  <div class="title-stamp"><h1>Velvet Hour Mixers</h1></div>

  <div class="schedule-bar"><p>Join us Fridays at 11:00 PM - 2:00 AM</p></div>

  <div class="venue">
    <svg class="venue-pin" viewBox="0 0 36 54" aria-hidden="true">
      <path d="M18 0 C22 14 36 26 36 38 A18 16 0 0 1 0 38 C0 26 14 14 18 0 Z" fill="var(--red)"/>
    </svg>
    <address class="venue-address">
      At<br>
      At The Quill Westbrook<br>
      27315 Harlow Ridge, Suite 340<br>
      Charlotte, NC 28193
    </address>
  </div>

  <p class="contact-lead">For more details email us at</p>
  <div class="contact-mail">
    <svg class="mail-icon" viewBox="0 0 38 24" aria-hidden="true">
      <rect x="0" y="0" width="38" height="24" fill="#c23a2c"/>
      <path d="M1 1 L19 14 L37 1" fill="none" stroke="var(--red)" stroke-width="2"/>
      <path d="M1 23 L14 11 M37 23 L24 11" fill="none" stroke="var(--red)" stroke-width="2"/>
    </svg>
    <span>info@lumora4.com</span>
  </div>
</main>
</body>
</html>
```